Golf Brochure + Business Card Design Project – Ridgeway Wellness.

Task Description

We are looking for a premium tri-fold brochure (8.5x11 letter, folded) plus a new business card design for Ridgeway Wellness. Both need to look polished, elegant, and professional — something that would feel at home in a golf club environment.

Brochure Scope:
• Tri-fold brochure promoting our new golf-specific services
• Incorporate brand colors: deep hunter green, cream, and gold accents
• Clean, modern typography (professional, not playful)
• Layout will follow the copy provided (final copy attached, no rewriting needed)
• Imagery: mature golfers (50+), golf lifestyle shots, no generic stocky images
• Include QR code placement linking to booking page
• Deliverables: print-ready PDF with bleed/crop (CMYK), high-res PDF (digital), and source file (InDesign or Illustrator)

Business Card Scope:
• Front + back design
• Consistent with brand colors and fonts
• Space for name, title, phone, email, and website
• Deliverables: print-ready PDF with bleed/crop (CMYK) + source file (AI or InDesign)
• If possible, provide editable template for future staff cards

Timeline:
• First draft within 5–7 days
• 2 rounds of revisions included

Budget:
$300 USD (total for both brochure + business card)

I’ll provide finalized copy if you accept the project.
Project description (paste this whole block in that box)

We need a premium tri-fold brochure (8.5”×11” letter, folded) and a new business card design for Ridgeway Wellness. This will be presented to golf course managers and members, so the look must be elegant, restrained, and country-club-classy.

Scope — Brochure
• Format: Tri-fold, 8.5”×11”. Please set 0.125” bleed on all sides and keep critical text ≥0.125–0.25” inside the trim.
• Purpose: Promote Ridgeway Wellness’ golf-specific services for adults 50+.
• Copy: We will provide finalized copy in a Word doc after acceptance. No rewriting needed — please focus on layout and polish.
• Imagery (required):
• Golf-first images (ball on tee/green, mature golfers mid-swing, and golf course landscapes at golden hour).
• 1–2 real Ridgeway Wellness gym photos on inside panels (trainer with client doing golf-relevant movement: stretch, rotation, balance).
• Visual style: Premium, quiet, lots of white/negative space, balanced grids; no clutter.
• Brand colors (required): Hunter Green #0C2E1F, Gold #CBA135, Cream #F5F2EB. Convert for CMYK print while preserving the look.
• Typography: Clean, legible serif + sans pairing (e.g., modern serif for headlines, humanist/neo-grotesk sans for body). You may propose suitable professional fonts; avoid playful/novelty fonts.
• Elements to include:
• Our logo (we will upload).
• QR code placement to booking page (we will supply the URL / QR asset).
• Simple icon treatment for the three complimentary options (Strength & Mobility, Stretch Therapy, Corvana + Assessment).
• Deliverables:
• Print-ready PDF (CMYK, with bleed & crop marks, PDF/X-1a or PDF/X-4)
• High-res digital PDF (no bleed)
• Source file (InDesign or Illustrator) + packaged fonts/links or outlined type as appropriate.

Scope — Business Card
• Size: 3.5”×2” (US standard) with 0.125” bleed; keep text ≥0.125” from trim.
• Front/back design; consistent with brochure branding.
• Fields: Name, Title, Phone, Email, Website, Address; optional small QR on back.
• Deliverables: Print-ready PDF (CMYK, bleed & crops) + Source file (AI/INDD). Provide an editable template for staff names.

Process & Timing
• Initial concept for brochure + card within 5–7 days of acceptance.
• 2 rounds of revisions included.
• Please start with a clean layout concept using placeholder images/text blocks; we’ll drop in final copy/assets immediately after acceptance.

Stock & Licensing
• You may propose stock images that fit the brief (we’re fine approving Pixelharbor or equivalent). Please note any license fees separately if needed.

Usage Rights
• We require full usage rights to the final designs for print & digital.

Target Market(s)

Golfers 50+ in Victoria, BC: quality-oriented, health-conscious, want to play longer, stronger, and pain-free. Country-club aesthetic; expect polished, professional materials.

Industry/Entity Type

Health & Fitness — Golf Performance / Longevity Studio

Font styles to use
Serif
Sans Serif

Requirements
Must have
• • Golf-first imagery + 1–2 real Ridgeway Wellness photos inside. • Brand colors: #0C2E1F (Hunter Green), #CBA135 (Gold), #F5F2EB (Cream). • Premium, restrained layout; ample negative space; no clutter. • Clean professional serif + sans type pairing; highly legible. • Space for logo and QR code (booking). • Correct print specs (bleed, crops, CMYK). • Deliverables: print-ready PDFs (brochure + card), digital PDF, source files.
Nice to have
• • Subtle texture or grain in backgrounds (very light) to add sophistication. • A second brochure cover variation (ball on tee vs. course landscape) at concept stage.
Should not have
• • Cheesy/posed “stocky” groups; overly young models; beer/alcohol imagery. • Over-saturated greens/blues; gimmicky gradients or clip art. • Generic fitness/bodybuilding shots unrelated to golf performance.

```html
<!DOCTYPE html>
<html lang="en">
<head>
<meta charset="utf-8">
<title>Ridgeway Wellness – Business Card</title>
<link rel="stylesheet" href="https://fonts.googleapis.com/css2?family=Jost:wght@300;400;500&display=swap">
<style>
  :root {
    --hunter: #0e3638;
    --cream: #f9f1e7;
    --paper: #ffffff;
    --ink: #0e3638;
    --light: #ffffff;
  }
  * { margin: 0; padding: 0; box-sizing: border-box; }
  html, body {
    width: 1055px;
    height: 1200px;
    overflow: hidden;
    background: var(--paper);
    font-family: "Jost", sans-serif;
  }
  .canvas {
    position: relative;
    width: 1055px;
    height: 1200px;
  }
  .card {
    position: absolute;
    width: 820px;
    height: 469px;
  }
  .card--front {
    left: 110px;
    top: 100px;
    background: var(--hunter);
    color: var(--light);
  }
  .card--back {
    left: 108px;
    top: 637px;
    background: var(--cream);
    color: var(--ink);
  }

  /* Front */
  .brand-lockup {
    position: absolute;
    left: 0;
    right: 0;
    top: 168px;
    display: flex;
    justify-content: center;
    align-items: center;
    gap: 14px;
  }
  .brand-lockup__dot {
    width: 18px;
    height: 18px;
    border-radius: 50%;
    background: var(--light);
  }
  .brand-lockup__name {
    font-weight: 500;
    font-size: 32px;
    letter-spacing: 0.14em;
    text-transform: uppercase;
    color: var(--light);
  }
  .tagline {
    position: absolute;
    left: 0;
    right: 0;
    top: 356px;
    display: flex;
    justify-content: center;
    align-items: center;
    font-weight: 300;
    font-size: 28px;
    line-height: 1;
  }
  .tagline__bullet {
    width: 10px;
    height: 10px;
    border-radius: 50%;
    background: var(--light);
    margin: 4px 38px 0;
  }

  /* Back */
  .contact-block {
    position: absolute;
    left: 0;
    right: 0;
    top: 82px;
    text-align: center;
  }
  .person-name {
    font-weight: 500;
    font-size: 40px;
    line-height: 1.2;
  }
  .person-title {
    margin-top: 10px;
    font-weight: 400;
    font-size: 17.5px;
    letter-spacing: 0.01em;
  }
  .person-title__divider {
    margin: 0 10px;
  }
  .contact-list {
    list-style: none;
    margin-top: 43px;
  }
  .contact-list__item {
    display: flex;
    flex-direction: column;
    align-items: center;
    font-weight: 400;
    font-size: 16.5px;
    line-height: 1.2;
  }
  .contact-list__item + .contact-list__item {
    margin-top: 22px;
  }
  .contact-list__icon {
    width: 17px;
    height: 17px;
    margin-bottom: 6px;
    stroke: var(--ink);
    fill: none;
    stroke-width: 1.3;
    stroke-linecap: round;
    stroke-linejoin: round;
  }
</style>
</head>
<body>
<main class="canvas">

  <section class="card card--front" aria-label="Card front">
    <div class="brand-lockup">
      <span class="brand-lockup__dot" aria-hidden="true"></span>
      <span class="brand-lockup__name">Ridgeway Wellness</span>
    </div>
    <p class="tagline">
      <span>Strength</span>
      <span class="tagline__bullet" aria-hidden="true"></span>
      <span>Mobility</span>
      <span class="tagline__bullet" aria-hidden="true"></span>
      <span>Longevity</span>
    </p>
  </section>

  <section class="card card--back" aria-label="Card back">
    <div class="contact-block">
      <h1 class="person-name">Marlowe-Anne Keating</h1>
      <p class="person-title">Owner<span class="person-title__divider">|</span>Ridgeway Wellness</p>

      <ul class="contact-list">
        <li class="contact-list__item">
          <svg class="contact-list__icon" viewBox="0 0 24 24" aria-hidden="true">
            <path d="M5 3h3.5l1.8 4.5-2.3 1.5a11 11 0 0 0 7 7l1.5-2.3L21 15.5V19a2 2 0 0 1-2 2A17 17 0 0 1 3 5a2 2 0 0 1 2-2z"/>
          </svg>
          <span>250-555-0147</span>
        </li>
        <li class="contact-list__item">
          <svg class="contact-list__icon" viewBox="0 0 24 24" aria-hidden="true">
            <rect x="2.5" y="5" width="19" height="14" rx="1"/>
            <path d="M3 6l9 7 9-7"/>
          </svg>
          <span>marlowe-anne@ridgewaywellness.biz</span>
        </li>
        <li class="contact-list__item">
          <svg class="contact-list__icon" viewBox="0 0 24 24" aria-hidden="true">
            <circle cx="12" cy="12" r="9.5"/>
            <ellipse cx="12" cy="12" rx="4.2" ry="9.5"/>
            <path d="M2.5 12h19M4 7h16M4 17h16M12 2.5v19"/>
          </svg>
          <span>ridgewaywellnessvictoria.com</span>
        </li>
      </ul>
    </div>
  </section>

</main>
</body>
</html>
```